Marlowe Tindra Pale Ale Beer Label/Badge

We need a Beer Label designed for our first official beer to be launched under The marlowe Brand!!
It will be a Pale Ale Called "Tindra Pale Ale"!

The Marlowe has the largest Craft Beer & Cider selection in the Geelong & Surf Coast region. With a funky location and a relaxed vibe, Marlowe prides itself on serving delicious, unique seasonal food paired with Australia's best Craft Beer. The marlowe is the perfect setting for a relaxed afternoon or evening with friends and can package an experience for larger groups or corporate bookings.

The Marlowe Tavern brand has been growing for over a year and a half and the first label needs to integrate The marlowe Logo but at the same time bring a fresh, new and eye catching feel to it along with embracing the "Odysseus" story in which we will be naming future beers.

The story of Tindra is found via the following link
http://en.lorevault.example/wiki/Tindra_(legend)

We expect designers to research The marlowe Tavern brand along with the all important Craft Beer Market and demographics. This will, potentially, be the start of many more labels to come for the winning designer!!

Requirements
Must have
• The original "O" needs to be integrated into the new logo and as much as the Greek mythology is being used it needs to be certain that this is an original Australian Craft Beer in the modern age!!
strong, modern & unique!!
Nice to have
• Logo could have a depiction of Tindra
Should not have
• tackiness or cheap!!

```html
<!DOCTYPE html>
<html lang="en">
<head>
<meta charset="utf-8">
<title>Marlowe Tindra Pale Ale – Label</title>
<link rel="stylesheet" href="https://fonts.googleapis.com/css2?family=Cinzel:wght@400;700&family=Lobster&display=swap">
<style>
  :root {
    --page: #ffffff;
    --label-red-dark: #7f241d;
    --label-red-light: #a9463b;
    --label-edge: #1b1210;
    --label-line: #ffffff;
    --type-white: #ffffff;
    --type-soft: #f3e4dd;
    --emblem-light: #d9a49b;
    --emblem-mid: #9c3b31;
  }
  html, body {
    margin: 0;
    padding: 0;
    overflow: hidden;
    background: var(--page);
  }
  .canvas {
    position: relative;
    width: 1200px;
    height: 1200px;
    background: var(--page);
    overflow: hidden;
  }
  .beer-label {
    position: absolute;
    left: 280px;
    top: 70px;
    width: 640px;
    height: 1060px;
    overflow: visible;
  }
  .label-body { fill: url(#labelRed); }
  .label-edge { fill: none; stroke: var(--label-edge); stroke-width: 16; stroke-linejoin: round; }
  .label-line { fill: none; stroke: var(--label-line); stroke-width: 7; stroke-linejoin: round; }
  .beer-name {
    font-family: "Lobster", cursive;
    font-size: 124px;
    fill: var(--type-white);
  }
  .beer-style {
    font-family: "Cinzel", serif;
    font-size: 46px;
    letter-spacing: 3px;
    fill: var(--type-soft);
  }
  .brewery-name {
    font-family: "Lobster", cursive;
    font-size: 42px;
    fill: var(--type-white);
  }
  .small-print {
    font-family: "Cinzel", serif;
    font-size: 16px;
    letter-spacing: 1px;
    fill: var(--type-soft);
  }
  .emblem { fill: url(#emblemTone); stroke: var(--label-line); stroke-width: 6; }
</style>
</head>
<body>
<main class="canvas">
  <svg class="beer-label" viewBox="0 0 640 1060" xmlns="http://www.w3.org/2000/svg">
    <defs>
      <linearGradient id="labelRed" x1="0" y1="0" x2="1" y2="0">
        <stop offset="0" stop-color="var(--label-red-dark)"/>
        <stop offset="0.55" stop-color="var(--label-red-light)"/>
        <stop offset="1" stop-color="var(--label-red-dark)"/>
      </linearGradient>
      <radialGradient id="emblemTone" cx="0.5" cy="0.5" r="0.5">
        <stop offset="0" stop-color="var(--emblem-light)"/>
        <stop offset="1" stop-color="var(--emblem-mid)"/>
      </radialGradient>
      <path id="labelOutline" d="M0,60 Q320,-20 640,60 L640,310 C640,345 600,340 600,380 C600,420 635,440 635,520 C635,600 600,620 600,660 C600,700 625,705 625,740 L625,810 C625,845 565,845 565,875 L565,1010 Q565,1040 535,1040 L105,1040 Q75,1040 75,1010 L75,875 C75,845 15,845 15,810 L15,740 C15,705 40,700 40,660 C40,620 5,600 5,520 C5,440 40,420 40,380 C40,340 0,345 0,310 Z"/>
    </defs>

    <g class="label-shape">
      <use href="#labelOutline" class="label-body"/>
      <use href="#labelOutline" class="label-edge"/>
      <use href="#labelOutline" class="label-line"/>
    </g>

    <text class="beer-name" x="320" y="190" text-anchor="middle">Tindra</text>
    <text class="beer-style" x="320" y="272" text-anchor="middle">PALE ALE</text>

    <circle class="emblem" cx="320" cy="520" r="160" role="img" aria-label="Badge emblem: serrated ring with a Greek key border around a profile portrait of Tindra"/>

    <text class="brewery-name" x="320" y="792" text-anchor="middle" textLength="540" lengthAdjust="spacingAndGlyphs">Marlowe Tavern &amp; Brewery</text>
    <text class="small-print" x="320" y="900" text-anchor="middle">MOUNT CARROW, VICTORIA, AUSTRALIA</text>
    <text class="small-print" x="320" y="950" text-anchor="middle">HANDCRAFTED BEER</text>
    <text class="small-print" x="320" y="1000" text-anchor="middle">ABV 5%</text>
  </svg>
</main>
</body>
</html>
```